Truck Wrap Design for Pell Rovey Haulers

We need a moving box truck wrapped with our catch phrase "We lift, We shift, we'll give your day a lift. Ring Pell Rovey!", our phone number "Call now (948) 312-8061, our FB page, instagram page, QR code, website: pellroveyhaulers.example, professional yet eye catching with our logo (uploaded). Truck information document attached as well showing dimensions of the vehicle. We would like some designs with color rather than black and white options.
Updates

Hey guys. We're really liking the efforts but would like to see more color in the designs. Something professional and simple.

Low design entry and low design quality submissions.

Target Market(s)

Families and older people

Industry/Entity Type

Moving

Requirements
Must have
• Contact information and catch phrase
Nice to have
• Professional and eye catching

```html
<!DOCTYPE html>
<html lang="en">
<head>
<meta charset="utf-8">
<title>Pell Rovey Haulers – Truck Wrap</title>
<link rel="stylesheet" href="https://fonts.googleapis.com/css2?family=Poppins:wght@400;500;600;700&display=swap">
<style>
  :root{
    --page:#eceef1;
    --wrap-black:#050608;
    --navy:#3c5079;
    --navy-deep:#2c3c5e;
    --white:#ffffff;
    --trim:#d9dbe0;
    --gold-light:#d8b877;
    --gold-dark:#9b7a3c;
    --cargo-light:#f4f4f4;
    --cargo-dark:#c9ccd1;
  }
  html,body{margin:0;padding:0;}
  body{
    width:1200px;height:1200px;overflow:hidden;
    background:var(--page);
    display:flex;flex-direction:column;align-items:center;justify-content:center;gap:70px;
    font-family:"Poppins",sans-serif;
  }
  .wrap-panel{display:block;width:1100px;height:458px;}
  .panel-base{fill:var(--wrap-black);}
  .panel-navy{fill:var(--navy);}
  .panel-trim{fill:var(--trim);}
  .tagline-bar{fill:var(--white);}
  .tagline{fill:var(--navy-deep);font-weight:600;font-size:7.6px;letter-spacing:.35px;}
  .brand-name{fill:var(--white);font-weight:500;font-size:27px;letter-spacing:1.8px;}
  .brand-mark{fill:none;stroke:var(--white);stroke-width:3;}
  .phone{fill:var(--white);font-weight:600;font-size:15px;letter-spacing:.3px;}
  .web{fill:var(--white);font-weight:400;font-size:9.5px;}
  .social-dot{fill:var(--white);}
  .phone-icon{fill:var(--white);}
</style>
</head>
<body>

<svg class="wrap-panel wrap-panel--gold" viewBox="0 0 600 250" role="group" aria-label="Truck wrap, gold cargo version">
  <defs>
    <linearGradient id="cargoGold" x1="0" y1="0" x2="1" y2="1">
      <stop offset="0" stop-color="var(--gold-light)"/>
      <stop offset="1" stop-color="var(--gold-dark)"/>
    </linearGradient>
  </defs>
  <rect class="panel-base" width="600" height="250"/>
  <polygon class="panel-navy" points="0,50 120,205 600,205 600,238 0,238"/>
  <rect role="img" aria-label="Illustration of a hand truck carrying stacked gold moving boxes" fill="url(#cargoGold)" x="18" y="14" width="196" height="200" rx="10"/>
  <rect class="tagline-bar" x="205" y="182" width="395" height="17"/>
  <text class="tagline" x="230" y="193.5">WE LIFT, WE SHIFT, WE'LL GIVE YOUR DAY A LIFT. RING PELL ROVEY!</text>
  <rect class="brand-mark" x="234" y="42" width="46" height="46"/>
  <text class="brand-name" x="440" y="80" text-anchor="middle">PELL ROVEY</text>
  <text class="brand-name" x="440" y="112" text-anchor="middle">HAULERS</text>
  <circle class="social-dot" cx="27" cy="222" r="6"/>
  <circle class="social-dot" cx="46" cy="222" r="6"/>
  <text class="phone" x="222" y="227">(948) 312-8061</text>
  <rect class="phone-icon" x="353" y="219" width="4" height="7" rx="1"/>
  <text class="web" x="363" y="226">www.<tspan font-weight="600">pellroveyhaulers</tspan>.example</text>
  <rect class="panel-trim" y="238" width="600" height="12"/>
</svg>

<svg class="wrap-panel wrap-panel--white" viewBox="0 0 600 250" role="group" aria-label="Truck wrap, white cargo version">
  <defs>
    <linearGradient id="cargoWhite" x1="0" y1="0" x2="1" y2="1">
      <stop offset="0" stop-color="var(--cargo-light)"/>
      <stop offset="1" stop-color="var(--cargo-dark)"/>
    </linearGradient>
  </defs>
  <rect class="panel-base" width="600" height="250"/>
  <polygon class="panel-navy" points="0,50 120,205 600,205 600,238 0,238"/>
  <rect role="img" aria-label="Illustration of a hand truck carrying stacked white moving boxes" fill="url(#cargoWhite)" x="18" y="14" width="196" height="200" rx="10"/>
  <rect class="tagline-bar" x="205" y="182" width="395" height="17"/>
  <text class="tagline" x="230" y="193.5">WE LIFT, WE SHIFT, WE'LL GIVE YOUR DAY A LIFT. RING PELL ROVEY!</text>
  <rect class="brand-mark" x="234" y="42" width="46" height="46"/>
  <text class="brand-name" x="440" y="80" text-anchor="middle">PELL ROVEY</text>
  <text class="brand-name" x="440" y="112" text-anchor="middle">HAULERS</text>
  <circle class="social-dot" cx="27" cy="222" r="6"/>
  <circle class="social-dot" cx="46" cy="222" r="6"/>
  <text class="phone" x="222" y="227">(948) 312-8061</text>
  <rect class="phone-icon" x="353" y="219" width="4" height="7" rx="1"/>
  <text class="web" x="363" y="226">www.<tspan font-weight="600">pellroveyhaulers</tspan>.example</text>
  <rect class="panel-trim" y="238" width="600" height="12"/>
</svg>

</body>
</html>
```